Renowned Chiropractic Clinic needs unique and professional business card

We need a clean and professional looking business card that embodies our core values and stands for excellence. Highest standard of care and trustworthiness is what we want a future patient to connect to the design of the business card.
Ideally we want the design of the business card to be unique in nature and have a close connection to the SPINE as it is the core of what we do in our office - working with peoples spines.

Contact Information for Business Card

Font file is modified Nexa light and Montserrat medium. Colors are #5BC9E1, #666666, and #9dd5eb

On the front we would like to have the logo and the name of the office with an engaging, trustworthy and professional design.
On the back we need an area for our address, phone number and email address (This can be also be in the front).
On the back we would also like the slogan (this is however not a must and can also be on the front).

The HEXAGON (the design from the spine), could be an idea for the design to evolve around - this is however up to your professional creativity!

Requirements
Must have
• I want the design to primarily evolve around the HEXAGON shape and to have as few curves in it as possible. Therefore, making the design as "edgy" and "linear" as possible.

- Logo
- German Address Line (we are moving offices so we do not yet have a physical address so it would have to be a placeholder address for now that can be changed) --> Office Name (Line 1), Streetname (Line 2), Zip Code and Town (Line 3)
- email and phone number field
Nice to have
• Incorporation of the slogan "Kehren Sie Ihren Problemen den Rücken"

Please let your imagination run free :)!!! I am excited to work with you all to create an astonishing business card!

```html
<!DOCTYPE html>
<html lang="de">
<head>
<meta charset="utf-8">
<title>Praxis Lotrecht – Visitenkarte</title>
<link rel="stylesheet" href="https://fonts.googleapis.com/css2?family=Montserrat:wght@400;500;600&display=swap">
<style>
  :root {
    --bg: #e9ebec;
    --card: #222222;
    --accent: #5bc9e1;
    --accent-soft: #9dd5eb;
    --text: #ffffff;
    --muted: #666666;
  }
  * { margin: 0; padding: 0; box-sizing: border-box; }
  html, body { width: 1200px; height: 912px; overflow: hidden; background: var(--bg); }
  body { font-family: "Montserrat", Arial, sans-serif; color: var(--text); position: relative; }

  .card {
    position: absolute;
    left: 250px;
    width: 700px;
    height: 400px;
    background: var(--card);
    border-radius: 22px;
    border-bottom: 5px solid var(--accent);
    overflow: hidden;
  }
  .card--front { top: 40px; }
  .card--back { top: 472px; }

  .brand {
    display: flex;
    align-items: center;
    gap: 16px;
    position: absolute;
    white-space: nowrap;
  }
  .brand__circle {
    width: 96px; height: 96px;
    border: 2px solid var(--accent);
    border-radius: 50%;
    flex: none;
  }
  .brand__name {
    font-weight: 500;
    color: var(--accent);
    font-size: 32px;
    letter-spacing: 3px;
    line-height: 1;
  }
  .card--front .brand { left: 130px; top: 110px; }

  .slogan {
    position: absolute;
    left: 0; right: 0;
    top: 290px;
    text-align: center;
    font-weight: 500;
    font-size: 17px;
    letter-spacing: 4.5px;
  }

  .card--back .brand { left: 40px; top: 168px; gap: 12px; }
  .card--back .brand__circle { width: 72px; height: 72px; }
  .card--back .brand__name { font-size: 19px; letter-spacing: 1.5px; }

  .divider {
    position: absolute;
    left: 388px; top: 70px;
    width: 2px; height: 260px;
    background: var(--accent);
  }

  .contact {
    position: absolute;
    left: 420px; top: 66px;
    font-weight: 500;
    font-size: 15px;
    line-height: 1.3;
  }
  .contact__name { color: var(--accent); font-weight: 600; font-size: 22px; letter-spacing: 0.5px; }
  .contact__role { font-size: 15px; margin-bottom: 20px; }
  .contact__address { margin-bottom: 20px; }
  .contact__list { list-style: none; }
  .contact__list li { display: flex; align-items: center; gap: 9px; }
  .contact__list svg { width: 13px; height: 13px; fill: var(--accent-soft); flex: none; }
  .contact__domain { color: var(--accent); font-style: normal; }
</style>
</head>
<body>

<section class="card card--front">
  <div class="brand">
    <span class="brand__circle"></span>
    <span class="brand__name">PRAXIS LOTRECHT</span>
  </div>
  <p class="slogan">Kehren Sie Ihren Problemen den Rücken</p>
</section>

<section class="card card--back">
  <div class="brand">
    <span class="brand__circle"></span>
    <span class="brand__name">PRAXIS LOTRECHT</span>
  </div>

  <span class="divider"></span>

  <div class="contact">
    <p class="contact__name">JONAS WERNER</p>
    <p class="contact__role">Creative Director</p>
    <p class="contact__address">PRAXIS LOTRECHT<br>Lindenallee 14<br>80331 München</p>
    <ul class="contact__list">
      <li><svg viewBox="0 0 16 16"><path d="M3 1h3l1.5 4-2 1.3a9 9 0 0 0 4.2 4.2L11 8.5l4 1.5v3a2 2 0 0 1-2 2A12 12 0 0 1 1 3a2 2 0 0 1 2-2z"/></svg><span>089-555-01240</span></li>
      <li><svg viewBox="0 0 16 16"><path d="M1 5c2-3 12-3 14 0v2h-4V5.5H5V7H1zM3 8h10l1 7H2z"/></svg><span>089-555-01370</span></li>
      <li><svg viewBox="0 0 16 16"><path d="M1 3h14v10H1zm1.5 1.5v.3L8 9l5.5-4.2v-.3z"/></svg><span>kontakt@praxis-lotrecht.de</span></li>
      <li><svg viewBox="0 0 16 16"><circle cx="8" cy="8" r="7"/></svg><span>www.<em class="contact__domain">praxis-lotrecht</em>.de</span></li>
    </ul>
  </div>
</section>

</body>
</html>
```